Awesome Office Furniture Dealer's Brochure!

Need a professional and informative brochure put together for our clients - may need separate designs for Government and Education clients. Should be based of our new website design and feel. Sections should include: Manufacturers we carry, services, and statements about our company - who we are & what we do. Brochure is 8.5 x 11 in tri-fold configuration. Template files attached.

Target Market(s)

Small to Medium businesses

Industry/Entity Type

Office Furniture

Requirements
Must have
• Look and feel of our website www.pembrills.com. Images can be taken from any of our vendors listed under /products, look to VEX primarily. We will get the final designer production ready images when needed.
Nice to have
• Incorporate the "love your workspace" from our website.

```html
<!DOCTYPE html>
<html lang="en">
<head>
<meta charset="utf-8">
<title>Pembrill's Office Furniture – Tri-fold Brochure</title>
<link href="https://fonts.googleapis.com/css2?family=Montserrat:wght@400;600;700;800&family=Open+Sans:wght@400;600;700&family=Kaushan+Script&display=swap" rel="stylesheet">
<style>
:root{
  --green:#8cc63f;
  --green-dark:#6fa52a;
  --charcoal:#58595b;
  --ink:#333;
  --muted:#666;
  --orange:#f26b21;
  --paper:#fff;
  --bg:#f2f2f2;
}
*{box-sizing:border-box;margin:0;padding:0}
html,body{width:784px;height:1200px;overflow:hidden;background:var(--bg)}
body{position:relative;font-family:"Open Sans",Arial,sans-serif;color:var(--ink)}
.spread{position:absolute;background:var(--paper);box-shadow:0 3px 10px rgba(0,0,0,.25);overflow:hidden}
.spread--outside{left:60px;top:40px;width:664px;height:500px}
.spread--inside{left:56px;top:640px;width:668px;height:515px}
.photo{position:absolute}
.abs{position:absolute}

/* outside */
.hero-band{left:0;top:0;width:221px;height:205px;background:var(--charcoal);padding:34px 22px}
.hero-title{font-family:"Montserrat",sans-serif;font-weight:400;color:#fff;font-size:23px;line-height:1.12;text-transform:uppercase}
.hero-title em{font-style:normal;font-weight:800;display:block}
.hero-title strong{font-weight:400;font-size:40px;display:block;margin-top:4px;letter-spacing:1px}
.brand{left:452px;top:22px;display:flex;align-items:center;gap:8px}
.brand-dot{width:24px;height:24px;border-radius:50%;background:var(--green)}
.brand-name{font-family:"Montserrat",sans-serif;font-weight:700;font-size:13px;color:var(--charcoal);line-height:1.05;text-transform:uppercase}
.footer-line{left:0;top:455px;width:250px;height:3px;background:var(--green)}
.footer-node{left:244px;top:450px;width:13px;height:13px;border-radius:50%;background:var(--green)}
.url{left:221px;top:466px;width:221px;text-align:center;font-family:"Montserrat",sans-serif;font-weight:700;font-size:9px;letter-spacing:1px;color:var(--green-dark)}
.tagline{right:22px;top:446px;font-family:"Kaushan Script",cursive;font-size:22px;color:var(--green)}

/* inside */
.why-text{left:14px;top:132px;width:196px;font-size:8.4px;line-height:1.4;color:var(--muted)}
.why-intro{text-align:center;font-size:9px;margin-bottom:10px;color:var(--ink)}
.why-intro b{color:var(--orange)}
.why-text p{margin-bottom:10px}
.why-text p b{color:var(--orange);font-weight:700}
.banner-title{left:300px;top:196px;width:138px;font-family:"Montserrat",sans-serif;font-weight:800;font-size:10px;color:#fff;text-transform:uppercase;line-height:1.25;text-align:right}
.do-it-all{left:222px;top:488px;width:224px;text-align:center;font-family:"Montserrat",sans-serif;font-weight:800;font-size:10px;color:var(--green-dark);letter-spacing:.5px}
.values{left:446px;top:0;width:222px;height:515px;background:var(--green);padding:26px 18px;color:#fff}
.values-title{font-family:"Montserrat",sans-serif;font-weight:800;font-size:15px;margin-bottom:16px;text-transform:uppercase;white-space:nowrap}
.value{margin-bottom:13px;text-align:center}
.value h3{font-size:8.8px;font-weight:700;margin-bottom:3px}
.value p{font-size:8px;line-height:1.4}
.call{left:572px;top:402px;width:86px;height:86px;border-radius:50%;background:#fff;color:var(--charcoal);text-align:center;padding-top:14px;font-size:8px;line-height:1.3}
.call b{display:block;font-size:8.5px;color:var(--ink)}
</style>
</head>
<body>

<section class="spread spread--outside" aria-label="Brochure outside">
  <div class="photo" role="img" aria-label="Bright open office with white desks and chairs" style="left:221px;top:0;width:221px;height:205px;background:linear-gradient(180deg,#ffffff 0%,#f4f5f5 45%,#d9dcdc 100%)"></div>
  <div class="photo" role="img" aria-label="White office with desks by a window" style="left:442px;top:70px;width:222px;height:135px;background:linear-gradient(180deg,#fbfbfb 0%,#eceeee 55%,#d2d6d6 100%)"></div>
  <div class="photo" role="img" aria-label="Conference room with long table and black chairs" style="left:0;top:205px;width:221px;height:225px;background:linear-gradient(180deg,#e6e8ea 0%,#b9bec2 50%,#5a5f63 100%)"></div>
  <div class="photo" role="img" aria-label="Office with glass walls and a potted plant" style="left:221px;top:205px;width:221px;height:225px;background:linear-gradient(180deg,#fafafa 0%,#e9ece8 55%,#a9b7a0 100%)"></div>
  <div class="photo" role="img" aria-label="Open plan workspace with grey desks" style="left:442px;top:205px;width:222px;height:225px;background:linear-gradient(180deg,#dfe2e3 0%,#c4c9cb 50%,#8d9497 100%)"></div>
  <svg class="abs" style="left:0;top:0" width="664" height="500" viewBox="0 0 664 500" aria-hidden="true">
    <polygon points="219,205 223,205 223,430 219,430" fill="#fff"/>
    <polygon points="440,205 444,205 444,430 440,430" fill="#fff"/>
    <rect x="0" y="203" width="664" height="4" fill="#fff"/>
    <polygon points="0,400 664,430 664,500 0,500" fill="#fff"/>
  </svg>
  <div class="abs hero-band">
    <h1 class="hero-title">We make <em>buying</em> office furniture <strong>easy</strong></h1>
  </div>
  <div class="abs brand"><span class="brand-dot"></span><span class="brand-name">Pembrill's<br>Office Furniture</span></div>
  <div class="abs footer-line"></div>
  <div class="abs footer-node"></div>
  <div class="abs url">WWW.PEMBRILLS.COM</div>
  <div class="abs tagline">Love your workspace!</div>
</section>

<section class="spread spread--inside" aria-label="Brochure inside">
  <div class="photo" role="img" aria-label="Breakout area with orange chairs and round white tables" style="left:0;top:0;width:222px;height:122px;background:linear-gradient(180deg,#f4f5f5 0%,#f6b27f 55%,#f07a2e 100%)"></div>
  <div class="abs why-text">
    <p class="why-intro">Why choose <b>Pembrill's office furniture?</b><br>Because we make office furniture easy.</p>
    <p><b>First,</b> we listen to what you need and bring over 25 years of commercial furniture experience to plan a space that truly works for your team.</p>
    <p><b>Second,</b> we carry the manufacturers you trust, from seating and desks to systems and storage, to fit any budget, timeline or style.</p>
    <p><b>Third,</b> we handle design, delivery and installation so your new workspace is ready on time and ready to use.</p>
    <p><b>Last,</b> we follow up after the move to make sure everything works well and your team loves the space.</p>
  </div>

  <div class="photo" role="img" aria-label="Bright glass atrium with a group of business people meeting" style="left:222px;top:0;width:224px;height:478px;background:linear-gradient(180deg,#ffffff 0%,#eef3f6 40%,#d5dfe5 70%,#aab6bd 100%)"></div>
  <svg class="abs" style="left:222px;top:0" width="224" height="515" viewBox="0 0 224 515" aria-hidden="true">
    <polygon points="0,0 4,0 4,478 0,478" fill="#fff"/>
    <polygon points="70,178 224,150 224,255 70,240" fill="var(--green)"/>
    <rect x="0" y="478" width="224" height="37" fill="#fff"/>
  </svg>
  <div class="abs banner-title">Products, solutions<br>&amp; services</div>
  <div class="abs do-it-all">YES, WE DO IT ALL!</div>

  <div class="abs values">
    <h2 class="values-title">Our core values</h2>
    <div class="value"><h3>Dedication to Customer Service Excellence</h3><p>We put our customers first and go beyond expectations on every single project we take on.</p></div>
    <div class="value"><h3>Honesty &amp; Integrity</h3><p>We do what we say, with open and honest communication at every step of the way.</p></div>
    <div class="value"><h3>People Growth &amp; Development</h3><p>We invest in our people so they can grow, learn and serve you even better.</p></div>
    <div class="value"><h3>Product Quality</h3><p>We offer quality products built to last, backed by trusted warranties and support.</p></div>
  </div>
  <div class="abs call">Call us @<b>Northgate</b>555-014-2200<b>Eastside</b>555-017-3300</div>
</section>

</body>
</html>
```